New web design needed for our company

We need our website designing, it needs to be professional and look creative,
We are a plumbing and heating company called Brackwell Flow's (www.brackwellflows.co.uk)
I like this site design also some of the following maybe:
https://www.tindermoorwarmth.com/
http://www.quorvapower.co.uk

Please let me know when you want our logo files as it wont let me upload them

The design will require coding once the design is complete, i havent paid for this yet as i want to be sure the design is good before i commit.

The template needs to look professional and look like one of the leading companies.
The site will consist of all the features this site has https://www.tindermoorwarmth.com/

I like a modern design with the latest technology.

Must have a customer login page and a my account area

Target Market(s)

Everyone

Industry/Entity Type

Plumbing

Coding

Coded - Design and coding required

Number of Pages Required

5+ page

Font styles to use
Other font styles liked:
• whatever suites

Requirements
Must have
• The design will require coding once the design is complete, i havent paid for this yet as i want to be sure the design is good before i commit.
• The template needs to look professional and look like one of the leading companies.
• The site will consist of all the features this site has https://www.tindermoorwarmth.com/
• I like a modern design with the latest technology.
• Must have a customer login page and a my account area
Nice to have
• inspirational and different
Should not have
• plain boring designs like most plumbing websites, needs to be inspiring and attract people from first sight.

```html
<!DOCTYPE html>
<html lang="en">
<head>
<meta charset="utf-8">
<title>Brackwell Flow's – Your Local Experts</title>
<link rel="stylesheet" href="https://fonts.googleapis.com/css2?family=Open+Sans:ital,wght@0,300;0,400;0,600;0,700;0,800;1,400&display=swap">
<style>
:root{
  --navy:#0f3376;
  --navy-dark:#0b2a63;
  --orange:#f15a3a;
  --text:#333a45;
  --muted:#777d86;
  --light:#eeeeee;
  --line:#dcdcdc;
  --white:#ffffff;
}
*{box-sizing:border-box;margin:0;padding:0}
html,body{width:1200px;height:3020px;overflow:hidden}
body{font-family:"Open Sans",Arial,sans-serif;color:var(--text);background:var(--white);position:relative}
.abs{position:absolute}
a{color:inherit;text-decoration:none}

/* header */
.brand{left:100px;top:34px}
.brand-name{font-size:50px;font-weight:800;color:var(--navy);letter-spacing:-1.5px;line-height:1;display:flex;align-items:center;gap:10px}
.brand-dot{width:22px;height:22px;border-radius:50%;background:var(--orange);display:inline-block}
.brand-tag{font-size:17px;color:var(--navy);margin-left:150px;margin-top:2px}
.topline{top:28px;left:680px;font-size:13px;color:var(--muted);display:flex;gap:28px;align-items:center}
.topline b{color:var(--orange);font-weight:600}
.topline span{display:flex;align-items:center;gap:8px}
.search{left:590px;top:73px;width:276px;height:36px;border:1px solid #cfd2d6;font-size:12px;color:#999;padding:10px 12px}
.search svg{position:absolute;right:10px;top:10px}
.btn-top{top:73px;height:36px;background:var(--orange);color:var(--white);font-size:12px;font-weight:700;display:flex;align-items:center;justify-content:center;gap:7px;border-radius:2px}
.sign{left:880px;width:82px}
.reg{left:986px;width:115px}

/* nav */
.nav{top:137px;left:0;width:1200px;height:46px;background:var(--navy)}
.nav ul{list-style:none;position:relative;height:46px}
.nav li{position:absolute;top:0;height:46px;line-height:46px;font-size:12.5px;font-weight:700;color:var(--white);text-transform:uppercase}
.nav li.active{background:var(--orange);left:100px;width:106px;text-align:center}

/* hero */
.hero{top:183px;left:0;width:1200px;height:527px;background:linear-gradient(180deg,#9eb7c9 0%,#7f8a8c 45%,#5d6e4c 78%,#4f7a35 100%)}
.hero-copy{left:90px;top:270px;width:300px;text-align:center;color:var(--white)}
.hero-kicker{font-size:30px;font-weight:700;letter-spacing:1px}
.hero-title{font-size:36px;font-weight:700;line-height:1.1}
.hero-text{font-size:14px;line-height:1.85;margin-top:12px}
.btn{background:var(--orange);color:var(--white);font-size:12.5px;font-weight:700;display:flex;align-items:center;justify-content:center;gap:9px;text-transform:uppercase;border-radius:2px}
.hero-btn{left:166px;top:463px;width:166px;height:42px}
.hero-arrow{left:40px;top:425px}

/* service cards */
.cards{top:610px;left:100px;width:1000px;height:282px;background:var(--white);box-shadow:0 4px 16px rgba(0,0,0,.14)}
.card{top:20px;width:310px;height:246px}
.card-img{height:180px}
.card-label{height:66px;background:var(--navy);color:var(--white);padding:13px 22px}
.card-label.hot{background:var(--orange)}
.card-label h3{font-size:15.5px;font-weight:700;text-transform:uppercase}
.card-label p{font-size:10.5px;font-weight:600;text-transform:uppercase;margin-top:6px;display:flex;align-items:center;gap:6px}

/* welcome */
.section-title{left:0;width:1200px;text-align:center;font-size:24px;font-weight:400;color:var(--navy);text-transform:uppercase;letter-spacing:.3px}
.section-title strong{font-weight:700}
.welcome-text{top:982px;left:240px;width:720px;text-align:center;font-size:14px;line-height:2;color:var(--muted)}
.welcome-text b{color:var(--orange);font-weight:400}
.w-btn{top:1060px;height:38px}

/* looking to do */
.tile{top:1218px;width:234px}
.tile-img{height:172px}
.tile-label{margin-top:20px;text-align:center;font-size:12.5px;font-weight:700;color:var(--navy-dark);text-transform:uppercase}
.chev{color:#b9bcc0}

/* video */
.video{top:1495px;left:0;width:1200px;height:405px;background:linear-gradient(100deg,#4d5a4b 0%,#a9a9a3 35%,#8a7466 65%,#b99a86 100%)}
.video-title{top:1722px;left:0;width:1200px;text-align:center;font-size:38px;font-weight:300;color:var(--white)}

/* news */
.news{width:470px;height:150px}
.news-img{width:170px;height:148px;position:absolute;left:0;top:0}
.news-body{position:absolute;left:198px;top:0;width:290px}
.news-body h4{font-size:13px;font-weight:700;color:var(--navy-dark);line-height:1.85;text-transform:uppercase}
.news-date{font-size:11.5px;color:var(--muted);margin:6px 0 8px;display:flex;align-items:center;gap:6px}
.news-body p{font-size:12.5px;line-height:1.85;color:var(--muted)}

/* testimonials */
.clients{top:2270px;left:0;width:1200px;height:360px;background:var(--light)}
.quote{width:300px}
.quote p{font-size:12.5px;font-style:italic;line-height:1.85;color:var(--muted);padding:0 30px}
.qmark{position:absolute;font-size:40px;color:#c4c6c9;font-family:Georgia,serif;line-height:1}
.person{position:absolute;top:122px;left:0;display:flex;align-items:center;gap:14px}
.avatar{width:58px;height:58px;border-radius:50%;border:3px solid var(--navy);background:#d6c6b6}
.person b{display:block;font-size:12.5px;color:var(--orange);font-weight:700;text-transform:uppercase}
.person span{font-size:11px;color:var(--muted)}

/* footer */
.foot-col{top:2686px}
.foot-col h5{font-size:13.5px;font-weight:700;color:var(--navy-dark);text-transform:uppercase;margin-bottom:10px}
.foot-col li{list-style:none;font-size:11.5px;color:#555b63;line-height:26.6px}
.foot-rule{top:2962px;left:0;width:1200px;height:1px;background:var(--line)}
.legal{top:2985px;font-size:11px;color:#555b63}
.legal b{color:var(--orange);font-weight:400}
</style>
</head>
<body>

<!-- header -->
<div class="abs brand">
  <div class="brand-name"><span class="brand-dot"></span>Brackwell Flow's</div>
  <div class="brand-tag">Your Local Experts</div>
</div>
<div class="abs topline">
  <span><svg width="18" height="18" viewBox="0 0 18 18"><circle cx="9" cy="10" r="7" fill="none" stroke="#f15a3a" stroke-width="1.6"/><path d="M9 6v4l3 2" stroke="#f15a3a" stroke-width="1.6" fill="none"/></svg>24 hours a day -7 day a week <b>Got a Question?</b></span>
  <span><svg width="20" height="18" viewBox="0 0 20 18"><path d="M1 2h3l2 10h11l2-7H5" fill="none" stroke="#f15a3a" stroke-width="1.6"/><circle cx="8" cy="15" r="1.5" fill="#f15a3a"/><circle cx="15" cy="15" r="1.5" fill="#f15a3a"/></svg>Cart is : <b>£ 0.00</b></span>
</div>
<div class="abs search">Search our site
  <svg width="14" height="14" viewBox="0 0 14 14"><circle cx="6" cy="6" r="4.5" fill="none" stroke="#999" stroke-width="1.5"/><path d="M9.5 9.5L13 13" stroke="#999" stroke-width="1.5"/></svg>
</div>
<a class="abs btn-top sign"><svg width="12" height="12" viewBox="0 0 12 12"><rect x="1" y="1" width="10" height="10" fill="none" stroke="#fff" stroke-width="1.4"/><path d="M3 6h5M6 4l2 2-2 2" stroke="#fff" stroke-width="1.4" fill="none"/></svg>SIGN IN</a>
<a class="abs btn-top reg"><svg width="12" height="12" viewBox="0 0 12 12"><rect x="1" y="1" width="10" height="10" fill="none" stroke="#fff" stroke-width="1.4"/><path d="M3 6h5M6 4l2 2-2 2" stroke="#fff" stroke-width="1.4" fill="none"/></svg>REGISTER</a>

<nav class="abs nav">
  <ul>
    <li class="active">Home</li>
    <li style="left:226px">My Account</li>
    <li style="left:366px">Services</li>
    <li style="left:482px">Emergencies</li>
    <li style="left:630px">Business Customers</li>
    <li style="left:826px">Pro Care</li>
    <li style="left:942px">Help and Support</li>
  </ul>
</nav>

<!-- hero -->
<div class="abs hero" role="img" aria-label="Large suburban family house with porch, surrounded by trees and a lawn"></div>
<svg class="abs hero-arrow" width="40" height="40" viewBox="0 0 40 40"><circle cx="20" cy="20" r="18" fill="none" stroke="rgba(255,255,255,.5)" stroke-width="1.5"/><path d="M23 13l-7 7 7 7" stroke="#fff" stroke-width="2" fill="none"/></svg>
<div class="abs hero-copy">
  <div class="hero-kicker">- FREE -</div>
  <div class="hero-title">Brewhill Coffee</div>
  <p class="hero-text">No more making the builder a drink,sit back and relax with free brewhill coffee while we do all the work.</p>
</div>
<a class="abs btn hero-btn">Find out more
  <svg width="13" height="13" viewBox="0 0 13 13"><circle cx="6.5" cy="6.5" r="6.5" fill="#fff"/><path d="M5 3.5l3 3-3 3" stroke="#f15a3a" stroke-width="1.6" fill="none"/></svg></a>

<!-- service cards -->
<section class="abs cards">
  <div class="abs card" style="left:18px">
    <div class="card-img" role="img" aria-label="Engineer repairing a boiler" style="background:linear-gradient(135deg,#4b4f57,#b2585a 55%,#d8d8d8)"></div>
    <div class="card-label hot"><h3>Boiler Repairs &amp; Maintenance</h3><p>Click here for view details <svg width="11" height="11" viewBox="0 0 11 11"><circle cx="5.5" cy="5.5" r="5.5" fill="#fff"/><path d="M4.3 3l2.5 2.5-2.5 2.5" stroke="#f15a3a" stroke-width="1.4" fill="none"/></svg></p></div>
  </div>
  <div class="abs card" style="left:346px">
    <div class="card-img" role="img" aria-label="Movers unloading boxes from a removal truck" style="background:linear-gradient(135deg,#c9c6c2,#a9a29a 60%,#8c7b6a)"></div>
    <div class="card-label"><h3>Moving Home?</h3><p>Click here for view details <svg width="11" height="11" viewBox="0 0 11 11"><circle cx="5.5" cy="5.5" r="5.5" fill="#fff"/><path d="M4.3 3l2.5 2.5-2.5 2.5" stroke="#0f3376" stroke-width="1.4" fill="none"/></svg></p></div>
  </div>
  <div class="abs card" style="left:674px">
    <div class="card-img" role="img" aria-label="Customer support agent wearing a headset in an office" style="background:linear-gradient(135deg,#e8ecef,#c7ced4 55%,#8e98a2)"></div>
    <div class="card-label"><h3>Got a Question?</h3><p>Click here for view details <svg width="11" height="11" viewBox="0 0 11 11"><circle cx="5.5" cy="5.5" r="5.5" fill="#fff"/><path d="M4.3 3l2.5 2.5-2.5 2.5" stroke="#0f3376" stroke-width="1.4" fill="none"/></svg></p></div>
  </div>
</section>

<!-- welcome -->
<h2 class="abs section-title" style="top:932px">Welcome to <strong>Brackwell Flows</strong></h2>
<p class="abs welcome-text">We know that moving home is stressful enough without worrying about your water supply – just give us a quick call on <b>0345 000 4821</b> and we'll make the whole thing as easy as possible.</p>
<a class="abs btn w-btn" style="left:453px;width:140px"><svg width="10" height="13" viewBox="0 0 10 13"><text x="3" y="11" fill="#fff" font-size="12" font-style="italic" font-weight="700" font-family="Georgia,serif">i</text></svg>Read more</a>
<a class="abs btn w-btn" style="left:608px;width:140px"><svg width="13" height="13" viewBox="0 0 13 13"><path d="M3 1l2 3-1.3 1.3c.8 1.7 2.2 3.1 3.9 3.9L9 8l3 2-1 2.3C6 12.5.5 7 .7 2z" fill="#fff"/></svg>Contact us</a>

<!-- looking to do -->
<h2 class="abs section-title" style="top:1152px">What are you <strong>looking to do?</strong></h2>
<svg class="abs chev" style="left:50px;top:1290px" width="16" height="30" viewBox="0 0 16 30"><path d="M14 1L2 15l12 14" stroke="#b9bcc0" stroke-width="1.6" fill="none"/></svg>
<svg class="abs chev" style="left:1134px;top:1290px" width="16" height="30" viewBox="0 0 16 30"><path d="M2 1l12 14L2 29" stroke="#b9bcc0" stroke-width="1.6" fill="none"/></svg>
<div class="abs tile" style="left:100px"><div class="tile-img" role="img" aria-label="Engineer in a hard hat holding a tablet" style="background:linear-gradient(135deg,#9fc3e3,#4f7fb5 60%,#e2a33b)"></div><div class="tile-label">Looking to do?</div></div>
<div class="abs tile" style="left:356px"><div class="tile-img" role="img" aria-label="Paperwork, glasses and a calculator on a desk" style="background:linear-gradient(135deg,#5d6b7a,#8a6a7a 55%,#3a5a8a)"></div><div class="tile-label">I need a landlord certificate</div></div>
<div class="abs tile" style="left:612px"><div class="tile-img" role="img" aria-label="Two engineers in hard hats reviewing plans" style="background:linear-gradient(135deg,#6f8a5a,#c9a54b 50%,#3d5f8f)"></div><div class="tile-label">Book an engineer</div></div>
<div class="abs tile" style="left:868px"><div class="tile-img" role="img" aria-label="Family looking at a laptop together at home" style="background:linear-gradient(135deg,#f0e6dc,#c9a28a 55%,#b35a4a)"></div><div class="tile-label">Manage your account</div></div>

<!-- how it works video -->
<div class="abs video" role="img" aria-label="Removal crew unloading a branded truck outside a brick house while a couple watches"></div>
<svg class="abs" style="left:556px;top:1636px" width="88" height="88" viewBox="0 0 88 88"><circle cx="44" cy="44" r="43" fill="#fff"/><path d="M36 28l22 16-22 16z" fill="#333a45"/></svg>
<div class="abs video-title">How it works</div>

<!-- latest news -->
<h2 class="abs section-title" style="top:1962px">Latest <strong>news</strong></h2>
<svg class="abs" style="left:50px;top:2105px" width="16" height="30" viewBox="0 0 16 30"><path d="M14 1L2 15l12 14" stroke="#b9bcc0" stroke-width="1.6" fill="none"/></svg>
<svg class="abs" style="left:1134px;top:2105px" width="16" height="30" viewBox="0 0 16 30"><path d="M2 1l12 14L2 29" stroke="#b9bcc0" stroke-width="1.6" fill="none"/></svg>
<article class="abs news" style="left:100px;top:2043px">
  <div class="news-img" role="img" aria-label="Technician working on machinery" style="background:linear-gradient(135deg,#4a5463,#8e7a6a 60%,#2c3440)"></div>
  <div class="news-body">
    <h4>Lorem Ipsum is simply dummy text of the printing</h4>
    <div class="news-date"><svg width="11" height="11" viewBox="0 0 11 11"><rect x="0.5" y="1.5" width="10" height="9" fill="none" stroke="#999"/><path d="M0.5 4h10" stroke="#999"/></svg>Posted on 27 May 2016</div>
    <p>Lorem Ipsum is simply dummy text of the printing and typesetting industry. Lorem Ipsum has been the industry's standard dummy...</p>
  </div>
</article>
<article class="abs news" style="left:622px;top:2043px">
  <div class="news-img" role="img" aria-label="Plumber fixing a kitchen tap" style="background:linear-gradient(135deg,#e4e8ec,#aab3bb 55%,#6c7a88)"></div>
  <div class="news-body">
    <h4>Lorem Ipsum is simply dummy text of the printing</h4>
    <div class="news-date"><svg width="11" height="11" viewBox="0 0 11 11"><rect x="0.5" y="1.5" width="10" height="9" fill="none" stroke="#999"/><path d="M0.5 4h10" stroke="#999"/></svg>Posted on 27 May 2016</div>
    <p>Lorem Ipsum is simply dummy text of the printing and typesetting industry. Lorem Ipsum has been the industry's standard dummy...</p>
  </div>
</article>

<!-- testimonials -->
<section class="abs clients">
  <h2 class="abs section-title" style="top:62px">What our <strong>client's say</strong></h2>
  <div class="abs quote" style="left:100px;top:124px">
    <span class="qmark" style="left:0;top:-6px">“</span><span class="qmark" style="right:0;top:62px">”</span>
    <p>Lorem Ipsum is simply dummy text of the printing and typesetting industry. Lorem Ipsum has been the industry's standard dummy text ever since the 1500s...</p>
    <div class="person"><div class="avatar" role="img" aria-label="Client portrait"></div><div><b>Marcus Ellery</b><span>Business man</span></div></div>
  </div>
  <div class="abs quote" style="left:450px;top:124px">
    <span class="qmark" style="left:0;top:-6px">“</span><span class="qmark" style="right:0;top:62px">”</span>
    <p>Lorem Ipsum is simply dummy text of the printing and typesetting industry. Lorem Ipsum has been the industry's standard dummy text ever since the 1500s...</p>
    <div class="person"><div class="avatar" role="img" aria-label="Client portrait" style="background:#e2cfa8"></div><div><b>Marcus Ellery</b><span>Business man</span></div></div>
  </div>
  <div class="abs quote" style="left:800px;top:124px">
    <span class="qmark" style="left:0;top:-6px">“</span><span class="qmark" style="right:0;top:62px">”</span>
    <p>Lorem Ipsum is simply dummy text of the printing and typesetting industry. Lorem Ipsum has been the industry's standard dummy text ever since the 1500s...</p>
    <div class="person"><div class="avatar" role="img" aria-label="Client portrait"></div><div><b>Marcus Ellery</b><span>Business man</span></div></div>
  </div>
</section>

<!-- footer -->
<footer>
  <div class="abs foot-col" style="left:107px"><h5>At Home</h5><ul><li>Moving Home</li><li>Our Guarantee</li><li>Charges</li><li>My Bill</li><li>Emergencies</li><li>Got a problem?</li></ul></div>
  <div class="abs foot-col" style="left:305px"><h5>Business Customers</h5><ul><li>Business services</li><li>Landlord services</li><li>Estate Agents</li><li>Property Contracts</li><li>Commercial Installations</li><li>Commercial Gas</li></ul></div>
  <div class="abs foot-col" style="left:588px"><h5>New Builds &amp; Construction</h5><ul><li>Heating and Water Design</li><li>Heating Technology</li><li>Housing Estates</li><li>Single Dwelling Install</li><li>Multi Dwelling Installs</li><li>Aftercare Guarantee</li></ul></div>
  <div class="abs foot-col" style="left:912px"><h5>Company</h5><ul><li>About us</li><li>Legal</li><li>Cookie policy</li><li>Terms &amp; conditions</li><li>Privacy policy</li><li>Access for everyone</li><li>Complaints procedure</li><li>Codes of practice</li></ul></div>
  <div class="abs foot-rule"></div>
  <div class="abs legal" style="left:100px">© 2016. Brackwell Flow's UK Limited. All rights reserved.</div>
  <div class="abs legal" style="left:780px">Registered in England and Wales Company number: <b>09273154</b></div>
  <div class="abs legal" style="left:1160px">C8</div>
</footer>

</body>
</html>
```